refresh/modernization of affiliate website template

Make this website look better. The site is comprised of various sections (nav, hero, products, FAQ, testimonials, gallery, contact us, blog listing page, single post page) that are modular in nature and it would be great if the genera template of the site was reusable with industries other than travel. We left the "look and feel" sliders in the neutral position because we are not too sure what we want and thus would like to see various approaches.

3 page

```html
<!DOCTYPE html>
<html lang="en">
<head>
<meta charset="utf-8">
<title>Trailmark Goods – Travel Products</title>
<link href="https://fonts.googleapis.com/css2?family=Montserrat:ital,wght@0,400;0,500;0,600;0,700;0,800;1,400&display=swap" rel="stylesheet">
<style>
:root{
  --green:#178a22;
  --lime:#8dc63f;
  --ink:#2b2b2b;
  --muted:#8a8a8a;
  --gray-bg:#f1f1f1;
  --footer:#333333;
  --white:#ffffff;
}
*{box-sizing:border-box;margin:0;padding:0}
html,body{width:1200px;height:4202px;overflow:hidden}
body{font-family:"Montserrat",sans-serif;color:var(--ink);background:var(--white);position:relative}
section,header,footer{position:absolute;left:0;width:1200px}
.abs{position:absolute}
a{text-decoration:none}
.btn{position:absolute;display:flex;align-items:center;justify-content:center;background:var(--green);color:var(--white);font-weight:700;text-transform:uppercase;letter-spacing:.3px;white-space:nowrap}
.btn-lime{background:var(--lime)}

.sec-title{position:absolute;left:0;width:100%;text-align:center;font-size:29px;line-height:36px;font-weight:700;letter-spacing:.5px;color:#333}
.sec-rule{position:absolute;left:50%;width:136px;margin-left:-68px;height:14px}
.sec-rule::before,.sec-rule::after{content:"";position:absolute;top:7px;width:50px;height:1px;background:#9a9a9a}
.sec-rule::before{left:0}.sec-rule::after{right:0}
.sec-rule span{position:absolute;left:61px;top:0;width:14px;height:14px;border-radius:50%;background:var(--lime)}

.site-nav{top:0;height:84px;background:var(--white)}
.brand{position:absolute;display:flex;align-items:center;gap:10px}
.brand-mark{width:30px;height:30px;border-radius:50%;background:var(--green);flex:none}
.brand-name{font-weight:800;font-size:22px;line-height:22px;color:var(--green);text-transform:uppercase;white-space:nowrap}
.nav-link{position:absolute;top:31px;font-size:14px;line-height:18px;color:#444;text-transform:uppercase;white-space:nowrap}

.hero{top:85px;height:535px}
.hero-photo{position:absolute;inset:0;background:linear-gradient(100deg,#f6f3ee 0%,#ece3d6 35%,#d9c8ad 55%,#bca784 72%,#e8dccb 88%,#c9b79b 100%)}
.hero-kicker{left:137px;top:162px;font-size:17px;line-height:20px;font-weight:700;color:var(--green);white-space:nowrap}
.hero-title{left:137px;top:190px;font-size:36px;font-weight:700;line-height:46px;color:#2e2e2e;white-space:nowrap}

.how{top:620px;height:547px}
.step{position:absolute;width:234px;height:234px;border-radius:50%;background:var(--white);box-shadow:0 10px 28px rgba(0,0,0,.12);display:flex;flex-direction:column;align-items:center;justify-content:center;text-align:center;color:var(--green);font-size:17px;font-weight:500;line-height:23px}
.step svg{margin-bottom:14px}

.products{top:1167px;height:608px;background:var(--gray-bg)}
.product{position:absolute;top:134px;width:218px;height:333px;background:var(--white);border:1px solid #cfcfcf}
.product-photo{position:absolute;left:0;top:0;width:216px;height:199px;background:var(--white)}
.product-name{position:absolute;left:20px;top:214px;font-size:12px;font-weight:700;line-height:16px;color:#222;white-space:nowrap}
.product-price{position:absolute;left:20px;top:248px;font-size:20px;line-height:24px;font-weight:700;color:var(--green);white-space:nowrap}
.product-price s{font-size:13px;color:#888;margin-left:4px;font-weight:600}
.product .btn{left:20px;top:287px;width:110px;height:28px;font-size:10px}

.tips{top:1775px;height:598px}
.tip{position:absolute;top:133px;width:304px;height:375px}
.tip-photo{position:absolute;left:0;top:0;width:304px;height:198px}
.tip-card{position:absolute;left:9px;top:170px;width:286px;height:205px;background:var(--white);box-shadow:0 4px 14px rgba(0,0,0,.12)}
.tip-date{position:absolute;left:88px;top:-12px;width:110px;height:26px;background:var(--lime);color:#1b3b0a;font-size:13px;font-weight:500;display:flex;align-items:center;justify-content:center;border-radius:3px}
.tip-title{position:absolute;left:30px;top:30px;font-size:16px;font-weight:700;line-height:18px;color:#2a2a2a;white-space:nowrap}
.tip-text{position:absolute;left:30px;top:78px;width:240px;font-size:11.5px;line-height:17px;color:#8b8b8b}
.tip .btn{left:30px;top:145px;width:110px;height:30px;font-size:11px}

.faq{top:2373px;height:530px;background:var(--gray-bg)}
.faq-photo{position:absolute;left:134px;top:103px;width:360px;height:360px;border-radius:50%;background:radial-gradient(circle at 50% 40%,#c9d2da 0%,#8f9aa4 45%,#59606a 100%);box-shadow:10px 6px 0 var(--lime)}
.faq-item{position:absolute;left:605px;width:461px;background:var(--white);border:2px solid #b6d97c;border-radius:3px}
.faq-q{position:absolute;left:22px;font-size:12.5px;line-height:16px;font-weight:700;color:#222;white-space:nowrap}
.faq-a{position:absolute;left:22px;top:40px;width:380px;font-size:11px;line-height:19px;color:#666}
.faq-item svg{position:absolute;right:22px}

.testi{top:2903px;height:486px}
.quote{position:absolute;top:166px;width:284px;height:176px;background:var(--white);box-shadow:0 4px 18px rgba(0,0,0,.1);border-radius:4px}
.quote-mark{position:absolute;left:20px;top:20px;font-size:44px;line-height:44px;color:var(--lime);font-family:Georgia,serif}
.quote-text{position:absolute;left:55px;top:26px;width:215px;font-size:12px;font-style:italic;line-height:24px;color:#9a9a9a;white-space:nowrap}
.author{position:absolute;top:363px;display:flex;align-items:center;gap:14px}
.avatar{width:48px;height:48px;border-radius:50%;background:linear-gradient(135deg,#777,#333)}
.author-name{font-size:14px;color:#333;white-space:nowrap}
.author-role{font-size:12px;color:#999;margin-top:5px;white-space:nowrap}

.contact{top:3389px;height:444px;background:linear-gradient(180deg,#178a22 0%,#1a8524 55%,#237a2a 100%)}
.contact .sec-title{color:var(--white);top:28px}
.contact .sec-rule::before,.contact .sec-rule::after{background:var(--white)}
.contact .sec-rule span{background:var(--white)}
.field{position:absolute;border:1.5px solid rgba(255,255,255,.85);color:var(--white);font-size:14px;padding-left:18px;display:flex;align-items:center}
.field-area{align-items:flex-start;padding-top:22px}
.send{position:absolute;left:510px;top:341px;width:162px;height:44px;border:2px solid var(--white);color:var(--white);font-size:17px;font-weight:600;display:flex;align-items:center;justify-content:center}
.to-top{position:absolute;left:1080px;top:3811px;width:40px;height:40px;border-radius:50%;background:var(--lime);display:flex;align-items:center;justify-content:center;z-index:2}

.site-footer{top:3833px;height:369px;background:var(--footer);color:var(--white)}
.foot-div{position:absolute;top:0;width:1px;height:232px;background:#5a5a5a}
.foot-head{position:absolute;top:70px;font-size:13px;line-height:16px;font-weight:700;text-transform:uppercase;white-space:nowrap}
.foot-head::before{content:"";position:absolute;left:-10px;top:0;width:2px;height:16px;background:var(--lime)}
.foot-links{position:absolute;top:100px;list-style:none;font-size:11px;line-height:26px;color:#e4e4e4}
.foot-small{position:absolute;font-size:9.5px;line-height:13px;color:#cfcfcf}
.social{position:absolute;top:102px;display:flex;gap:7px}
.social span{width:24px;height:24px;border-radius:50%;background:var(--white)}
.sub-input{position:absolute;left:856px;top:94px;width:204px;height:34px;background:var(--white);color:#777;font-size:11px;display:flex;align-items:center;padding-left:16px}
</style>
</head>
<body>

<header class="site-nav">
  <div class="brand" style="left:93px;top:19px">
    <span class="brand-mark"></span>
    <span class="brand-name">Trailmark<br>Goods</span>
  </div>
  <a class="nav-link" style="left:352px">Travel Products</a>
  <a class="nav-link" style="left:564px">Blogs</a>
  <a class="nav-link" style="left:681px">Testimonials</a>
  <a class="nav-link" style="left:859px">FAQ</a>
  <a class="btn" style="left:954px;top:21px;width:155px;height:39px;font-size:14px">Contact</a>
</header>

<section class="hero">
  <div class="hero-photo" role="img" aria-label="Traveller walking with a rolling suitcase through a sunlit airport terminal"></div>
  <p class="abs hero-kicker">WELCOME TO TRAILMARK GOODS</p>
  <h1 class="abs hero-title">UNLOCK THE<br>WORLD WITH STYLE</h1>
  <a class="btn" style="left:139px;top:298px;width:161px;height:36px;font-size:15px">Shop Now</a>
</section>

<section class="how">
  <h2 class="sec-title" style="top:48px">HOW IT WORKS</h2>
  <div class="sec-rule" style="top:92px"><span></span></div>
  <svg class="abs" style="left:0;top:0" width="1200" height="547" viewBox="0 0 1200 547" aria-hidden="true">
    <g fill="none" stroke="var(--green)" stroke-width="2">
      <path d="M184 368 A135 135 0 1 1 452 270"/>
      <path d="M456 270 A145 145 0 0 0 738 362"/>
      <path d="M745 362 A135 135 0 1 1 1030 342"/>
    </g>
    <circle cx="184" cy="368" r="5" fill="var(--lime)"/>
    <circle cx="1030" cy="342" r="5" fill="var(--lime)"/>
    <path d="M447 266 l12 0 -6 11z" fill="var(--lime)"/>
    <path d="M732 360 l12 -6 -2 12z" fill="var(--green)"/>
  </svg>
  <div class="step" style="left:189px;top:173px">
    <svg width="44" height="40" viewBox="0 0 44 40" fill="none" stroke="var(--green)" stroke-width="2"><rect x="3" y="3" width="38" height="26"/><path d="M16 37h12M22 29v8"/><rect x="9" y="9" width="14" height="10"/><path d="M27 11h8M27 16h8"/></svg>
    TRAVEL TIPS
  </div>
  <div class="step" style="left:484px;top:173px">
    <svg width="44" height="40" viewBox="0 0 44 40" fill="none" stroke="var(--green)" stroke-width="2"><path d="M6 12l16-8 16 8v20l-16 6-16-6z"/><path d="M6 12l16 8 16-8M22 20v18"/></svg>
    REQUENTLY ASKED<br>QUETIONS
  </div>
  <div class="step" style="left:771px;top:173px">
    <svg width="44" height="40" viewBox="0 0 44 40" fill="none" stroke="var(--green)" stroke-width="2"><rect x="4" y="12" width="26" height="20"/><path d="M12 38h10M17 32v6"/><circle cx="34" cy="10" r="6"/><path d="M10 20h14M10 25h9"/></svg>
    TRAVEL PRODDUCTS
  </div>
</section>

<section class="products">
  <h2 class="sec-title" style="top:48px">TRAVEL PRODUCTS</h2>
  <div class="sec-rule" style="top:92px"><span></span></div>

  <article class="product" style="left:152px">
    <div class="product-photo" role="img" aria-label="Turquoise travel neck pillow" style="background:radial-gradient(circle at 50% 48%,#6ad9cc 0%,#3cc2b3 38%,#fff 40%)"></div>
    <p class="product-name">LOREM IPSUM DOLOR SIT<br>AMET CONSECTETUR</p>
    <p class="product-price">₹459.00<s>₹500.00</s></p>
    <a class="btn btn-lime">Shop Now</a>
  </article>
  <article class="product" style="left:386px">
    <div class="product-photo" role="img" aria-label="Blue hard-shell suitcase" style="background:linear-gradient(#fff 20%,#3b97e0 20%,#2a7fcf 78%,#fff 78%) 76px 0/64px 100% no-repeat,#fff"></div>
    <p class="product-name">LOREM IPSUM DOLOR SIT<br>AMET CONSECTETUR</p>
    <p class="product-price">₹459.00<s>₹500.00</s></p>
    <a class="btn btn-lime">Shop Now</a>
  </article>
  <article class="product" style="left:616px">
    <div class="product-photo" role="img" aria-label="Yellow suitcase with sun hat and sandals" style="background:linear-gradient(#fff 22%,#f3d33a 22%,#e5bf1f 78%,#fff 78%) 72px 0/72px 100% no-repeat,#fff"></div>
    <p class="product-name">LOREM IPSUM DOLOR SIT<br>AMET CONSECTETUR</p>
    <p class="product-price">₹459.00<s>₹500.00</s></p>
    <a class="btn btn-lime">Shop Now</a>
  </article>
  <article class="product" style="left:851px">
    <div class="product-photo" role="img" aria-label="Teal hard-shell suitcase" style="background:linear-gradient(#fff 20%,#3fd0bd 20%,#2cb7a5 78%,#fff 78%) 76px 0/64px 100% no-repeat,#fff"></div>
    <p class="product-name">LOREM IPSUM DOLOR SIT<br>AMET CONSECTETUR</p>
    <p class="product-price">₹459.00<s>₹500.00</s></p>
    <a class="btn btn-lime">Shop Now</a>
  </article>

  <svg class="abs" style="left:78px;top:257px" width="28" height="40" viewBox="0 0 28 40" aria-hidden="true"><path d="M22 4L6 20l16 16" fill="none" stroke="#999" stroke-width="4"/></svg>
  <svg class="abs" style="left:1096px;top:257px" width="28" height="40" viewBox="0 0 28 40" aria-hidden="true"><path d="M6 4l16 16L6 36" fill="none" stroke="#999" stroke-width="4"/></svg>

  <a class="btn" style="left:523px;top:509px;width:166px;height:44px;font-size:15px">View More</a>
</section>

<section class="tips">
  <h2 class="sec-title" style="top:48px">TRAVEL TIPS</h2>
  <div class="sec-rule" style="top:92px"><span></span></div>

  <article class="tip" style="left:137px">
    <div class="tip-photo" role="img" aria-label="Suitcases by an airport window with a plane outside" style="background:linear-gradient(135deg,#cfd8df,#8a9aa6 60%,#4e5e68)"></div>
    <div class="tip-card">
      <span class="tip-date">JAN 20, 2023</span>
      <h3 class="tip-title">Duis non nunc Nulla rho<br>ncus dictum metus</h3>
      <p class="tip-text">Vivamus porttitor purus nisi eleifend libero a tempus libero lectus feugiat felis Morbi diam mauris viverra in gra</p>
      <a class="btn btn-lime">Read More</a>
    </div>
  </article>
  <article class="tip" style="left:448px">
    <div class="tip-photo" role="img" aria-label="Traveller in orange top with a blue suitcase against a dark wall" style="background:linear-gradient(135deg,#4a4a4a,#2c2c2c 60%,#d86a3a 61%,#2c2c2c 75%)"></div>
    <div class="tip-card">
      <span class="tip-date">JAN 20, 2023</span>
      <h3 class="tip-title">Duis non nunc Nulla rho<br>ncus dictum metus</h3>
      <p class="tip-text">Vivamus porttitor purus nisi eleifend libero a tempus libero lectus feugiat felis Morbi diam mauris viverra in gra</p>
      <a class="btn btn-lime">Read More</a>
    </div>
  </article>
  <article class="tip" style="left:760px">
    <div class="tip-photo" role="img" aria-label="Open suitcase being packed with clothes, hat and sunglasses" style="background:linear-gradient(135deg,#d9c9b4,#b7a592 45%,#7c8b96)"></div>
    <div class="tip-card">
      <span class="tip-date">JAN 20, 2023</span>
      <h3 class="tip-title">Duis non nunc Nulla rho<br>ncus dictum metus</h3>
      <p class="tip-text">Vivamus porttitor purus nisi eleifend libero a tempus libero lectus feugiat felis Morbi diam mauris viverra in gra</p>
      <a class="btn btn-lime">Read More</a>
    </div>
  </article>
</section>

<section class="faq">
  <h2 class="sec-title" style="top:48px">FREQUENTLY ASKED QUESTIONS</h2>
  <div class="sec-rule" style="top:92px"><span></span></div>
  <div class="faq-photo" role="img" aria-label="Traveller walking through an airport pulling red, pink and blue suitcases"></div>

  <div class="faq-item" style="top:141px;height:92px">
    <p class="faq-q" style="top:20px">Lorem Ipsum has been the industry's standard ?</p>
    <p class="faq-a">Lorem Ipsum has been the industry's standard dummy text ever since the 1500s, when an unknown</p>
    <svg style="top:20px" width="14" height="10" viewBox="0 0 14 10" aria-hidden="true"><path d="M1 8l6-6 6 6" fill="none" stroke="#444" stroke-width="1.6"/></svg>
  </div>
  <div class="faq-item" style="top:245px;height:48px">
    <p class="faq-q" style="top:14px">What can I do to improve trailmark goods ?</p>
    <svg style="top:17px" width="14" height="10" viewBox="0 0 14 10" aria-hidden="true"><path d="M1 2l6 6 6-6" fill="none" stroke="#444" stroke-width="1.6"/></svg>
  </div>
  <div class="faq-item" style="top:304px;height:48px">
    <p class="faq-q" style="top:14px">Lorem Ipsum has been the?</p>
    <svg style="top:17px" width="14" height="10" viewBox="0 0 14 10" aria-hidden="true"><path d="M1 2l6 6 6-6" fill="none" stroke="#444" stroke-width="1.6"/></svg>
  </div>
  <div class="faq-item" style="top:366px;height:48px">
    <p class="faq-q" style="top:14px">Lorem Ipsum has been the industry ?</p>
    <svg style="top:17px" width="14" height="10" viewBox="0 0 14 10" aria-hidden="true"><path d="M1 2l6 6 6-6" fill="none" stroke="#444" stroke-width="1.6"/></svg>
  </div>
</section>

<section class="testi">
  <h2 class="sec-title" style="top:60px">TESTIMONIALS</h2>
  <div class="sec-rule" style="top:106px"><span></span></div>

  <blockquote class="quote" style="left:135px"><span class="quote-mark">“</span><p class="quote-text">On a clerical level, I think that it will<br>be massive for our office staff. I<br>think that it will improve<br>inter-departmental<br>communications.</p></blockquote>
  <blockquote class="quote" style="left:460px"><span class="quote-mark">“</span><p class="quote-text">On a clerical level, I think that it will<br>be massive for our office staff. I<br>think that it will improve<br>inter-departmental<br>communications.</p></blockquote>
  <blockquote class="quote" style="left:782px"><span class="quote-mark">“</span><p class="quote-text">On a clerical level, I think that it will<br>be massive for our office staff. I<br>think that it will improve<br>inter-departmental<br>communications.</p></blockquote>

  <div class="author" style="left:143px"><span class="avatar" role="img" aria-label="Customer portrait"></span><div><p class="author-name">Dana Hollis</p><p class="author-role">Sep 2023, Captain</p></div></div>
  <div class="author" style="left:467px"><span class="avatar" role="img" aria-label="Customer portrait"></span><div><p class="author-name">Marco Velez</p><p class="author-role">Sep 2023, Captain</p></div></div>
  <div class="author" style="left:790px"><span class="avatar" role="img" aria-label="Customer portrait"></span><div><p class="author-name">Dana Hollis</p><p class="author-role">Sep 2023, Captain</p></div></div>
</section>

<section class="contact">
  <h2 class="sec-title">CONTACT US</h2>
  <div class="sec-rule" style="top:72px"><span></span></div>
  <div class="field" style="left:230px;top:121px;width:357px;height:44px">First Name</div>
  <div class="field" style="left:597px;top:121px;width:358px;height:44px">Last Name</div>
  <div class="field" style="left:230px;top:173px;width:357px;height:44px">Email address</div>
  <div class="field" style="left:597px;top:173px;width:358px;height:44px">Phone Number</div>
  <div class="field field-area" style="left:230px;top:231px;width:725px;height:97px">Type Message</div>
  <div class="send">SEND</div>
</section>

<a class="to-top" aria-label="Back to top"><svg width="16" height="18" viewBox="0 0 16 18" aria-hidden="true"><path d="M8 17V2M2 8l6-6 6 6" fill="none" stroke="#fff" stroke-width="1.8"/></svg></a>

<footer class="site-footer">
  <div class="brand" style="left:139px;top:58px">
    <span class="brand-mark" style="background:var(--white)"></span>
    <span class="brand-name" style="color:var(--white)">Trailmark<br>Goods</span>
  </div>
  <p class="foot-small" style="left:135px;top:112px;width:220px">Lorem ipsum dolor sit amet, consectetur adipiscing elit, sed do eiusmod tempor incididunt ut labore et dolore</p>
  <p class="foot-small" style="left:135px;top:162px;white-space:nowrap">© 2022 <u>TrailmarkGoods</u>. All Rights Reserved</p>

  <span class="foot-div" style="left:417px"></span>
  <span class="foot-div" style="left:600px"></span>
  <span class="foot-div" style="left:830px"></span>

  <h4 class="foot-head" style="left:443px">Quick Links</h4>
  <ul class="foot-links" style="left:445px">
    <li>Home</li><li>Products</li><li>FAQ</li><li>Blogs</li><li>Testimonials</li><li>Contact Us</li>
  </ul>

  <h4 class="foot-head" style="left:629px">Get in Touch</h4>
  <div class="social" style="left:629px"><span></span><span></span><span></span><span></span></div>
  <svg class="abs" style="left:629px;top:143px" width="26" height="26" viewBox="0 0 26 26" aria-hidden="true"><circle cx="13" cy="13" r="13" fill="#fff"/><rect x="7" y="9" width="12" height="9" fill="none" stroke="#333" stroke-width="1.5"/><path d="M7 9l6 5 6-5" fill="none" stroke="#333" stroke-width="1.5"/></svg>
  <p class="foot-small" style="left:664px;top:144px;color:#fff;font-weight:700;white-space:nowrap">Email address</p>
  <p class="foot-small" style="left:664px;top:158px;color:#e4e4e4;white-space:nowrap">hello@trailmarkgoods.com</p>

  <h4 class="foot-head" style="left:856px">Subscribe for Deals</h4>
  <div class="sub-input">Email address</div>
  <a class="btn" style="left:856px;top:136px;width:204px;height:33px;font-size:11px">Subscribe</a>
</footer>

</body>
</html>
```